Tarbery's - Irish Shortbread

Tarbery’s Irish Shortbread
We are looking for a Stand-Up Pouch design – (no window no zip) that will have different flavoured all-butter shortbread in the collection. We love vintage and kitsch as a company but do not have to head in that direction. We are font lovers and would happily have a Font Driven Design for packaging. For this project we were thinking about water colours to define the flavours or Graffiti Package Design. We have 6 flavours, they are:
Irish Shortbread - Ginger Shortbread - Espresso Shortbread - Parmesan and Poppy Seed Shortbread - Strawberry Shortbread - Butterscotch Shortbread.
The size of the pouch is 12cm x 17 cm. There needs to be a hanging hole at the top. We have uploaded a couple of images. What we like is the intensity of colour, clarity of flavour and words. This needs to feel familiar yet fresh on the shelf and not merge with other packaging at the supermarket.
We are also fans of 80s Graffiti designs for packaging – see a few attached images.
I have also attached the brand

```html
<!DOCTYPE html>
<html lang="en">
<head>
<meta charset="utf-8">
<title>Tarbery's Irish Shortbread – Pouch Front</title>
<link href="https://fonts.googleapis.com/css2?family=Montserrat:wght@500;600&family=Lora:wght@700&family=Permanent+Marker&display=swap" rel="stylesheet">
<style>
  :root {
    --backdrop: #afc5cb;
    --pouch: #f4f4f5;
    --pouch-edge: #e3e3e6;
    --ink: #1d1d1f;
    --pink-light: #f6cfe0;
    --pink-mid: #ee9cc2;
    --pink-deep: #e878ad;
    --band: #c04fa6;
    --white: #ffffff;
    --badge-red: #d7262f;
  }
  * { margin: 0; padding: 0; box-sizing: border-box; }
  html, body { width: 1200px; height: 1200px; overflow: hidden; }
  body { background: var(--backdrop); position: relative; font-family: "Montserrat", sans-serif; color: var(--ink); }

  .pouch {
    position: absolute; left: 258px; top: 106px; width: 684px; height: 1000px;
    background: var(--pouch); border-radius: 22px 22px 12px 12px; overflow: hidden;
  }
  .hang-hole {
    position: absolute; left: 321px; top: 38px; width: 30px; height: 30px;
    border-radius: 50%; background: var(--backdrop);
  }
  .seal-line {
    position: absolute; left: 0; right: 0; top: 78px; height: 8px;
    border-top: 1px solid var(--pouch-edge); border-bottom: 1px solid var(--pouch-edge);
  }
  .origin-badge {
    position: absolute; left: 526px; top: 120px; width: 104px; height: 104px;
    border-radius: 50%; border: 4px solid var(--badge-red);
  }
  .brand-name {
    position: absolute; left: 0; right: 0; top: 260px; text-align: center;
    font-family: "Montserrat", sans-serif; font-weight: 600; font-size: 92px; letter-spacing: -1px;
    color: var(--ink);
  }
  .brand-name::after {
    content: ""; display: block; width: 330px; height: 4px; margin: 8px auto 0;
    background: var(--ink); border-radius: 4px;
  }
  .tagline {
    position: absolute; left: 0; right: 0; top: 432px; text-align: center;
    font-weight: 500; font-size: 20px; letter-spacing: 4px;
  }
  .flavour-wash {
    position: absolute; left: 0; right: 0; top: 540px; bottom: 0;
    background: linear-gradient(180deg, rgba(246,207,224,0) 0%, var(--pink-light) 14%, var(--pink-mid) 60%, var(--pink-deep) 100%);
  }
  .flavour-band {
    position: absolute; left: 48px; right: 48px; top: 646px; height: 86px;
    background: var(--band); display: flex; align-items: center; justify-content: center;
  }
  .flavour-name {
    font-family: "Permanent Marker", cursive; font-size: 62px; color: var(--white); line-height: 1;
  }
  .pack-info {
    position: absolute; left: 0; right: 0; top: 746px; text-align: center;
    font-family: "Lora", serif; font-weight: 700; font-size: 22px;
  }
  .claims {
    position: absolute; left: 0; right: 0; top: 820px;
    display: flex; justify-content: center; gap: 22px;
  }
  .claim {
    width: 74px; height: 74px; border-radius: 50%; border: 3px solid var(--ink);
    display: flex; align-items: center; justify-content: center; text-align: center;
    font-size: 9px; font-weight: 600; line-height: 1.15; text-transform: uppercase;
  }
  .net-weight {
    position: absolute; left: 0; right: 0; top: 916px; text-align: center;
    font-family: "Lora", serif; font-weight: 700; font-size: 20px;
  }
</style>
</head>
<body>
  <div class="pouch">
    <div class="hang-hole"></div>
    <div class="seal-line"></div>
    <div class="origin-badge" role="img" aria-label="Country of origin badge"></div>

    <div class="brand-name">Tarbery’s</div>
    <div class="tagline">all butter goodness</div>

    <div class="flavour-wash" role="img" aria-label="Pink watercolour wash for the flavour"></div>
    <div class="flavour-band"><span class="flavour-name">Irish Shortbread</span></div>
    <div class="pack-info">12 Cookies | Bite Size</div>

    <div class="claims">
      <div class="claim">No<br>Additives</div>
      <div class="claim">No Added<br>Preser&shy;vatives</div>
      <div class="claim">No Added<br>Colours</div>
      <div class="claim">All<br>Butter</div>
    </div>

    <div class="net-weight">Net Wt 144g</div>
  </div>
</body>
</html>
```